International Biotech Startup needs a professionally looking web Design

We need a web design for a small biotech company based in Singapore which has global Pharma and Biotech Customers.

Our current website: www.velquorlabs.com

However this was generated by few of us. We would require a professional design for biotech companies like us. The appearance of the website should be appealing to users and this is mainly a promotional website without any financial transactions.
Once the design is approved, we will provide the updated text.

Target Market(s)

Pharmaceutical, Biotech, healthcare

Industry/Entity Type

Biotechnology

Coding

Coded - Design and coding required

Number of Pages Required

5+ page

Requirements
Must have
• the website needs favicon.
Nice to have
• Please some of the companies websites that we like the most or they are in the similar domain. We would like to have something like that:
• http://www.tarnwickbioscience.com/
• http://www.brisaltherapeutics.com/
• http://www.elumbo.com/
• http://www.fendral.com/
• www.plumvasi.com

```html
<!DOCTYPE html>
<html lang="en">
<head>
<meta charset="utf-8">
<title>Velquor Labs — Synthetic Biology Company</title>
<link href="https://fonts.googleapis.com/css2?family=Montserrat:wght@400;500;700&display=swap" rel="stylesheet">
<style>
  :root{
    --hero-grey:#a7a7a7;
    --white:#ffffff;
    --section-light:#f5f4f5;
    --ink:#2b2b2b;
    --ink-soft:#4a4a4a;
    --navy:#0c1842;
    --navy-deep:#060a2a;
    --contact-tint:#e1f0f3;
    --field-line:#5d6a72;
    --footer:#282828;
    --footer-text:#e6e6e6;
  }
  *{box-sizing:border-box;margin:0;padding:0}
  html,body{width:788px;height:1200px;overflow:hidden}
  body{font-family:"Montserrat",Arial,sans-serif;color:var(--ink);position:relative;background:var(--white)}

  .hero{position:absolute;left:0;top:0;width:788px;height:433px;background:var(--hero-grey)}
  .hero-art{position:absolute;left:55px;top:50px;width:650px;height:345px;
    background:radial-gradient(ellipse at 18% 48%,rgba(40,30,150,.75),rgba(40,30,150,0) 45%),
               radial-gradient(ellipse at 50% 30%,rgba(110,30,90,.6),rgba(110,30,90,0) 40%),
               radial-gradient(ellipse at 78% 58%,rgba(170,20,30,.75),rgba(170,20,30,0) 42%);}
  .brand{position:absolute;left:158px;top:18px;display:flex;align-items:center;gap:5px;color:var(--white);font-weight:700;font-size:17px;letter-spacing:.5px}
  .brand-dot{width:9px;height:9px;border-radius:50%;background:var(--white)}
  .main-nav{position:absolute;top:29px;left:382px;display:flex;gap:15px}
  .main-nav a{color:var(--white);text-decoration:none;font-size:6px;letter-spacing:.4px}
  .hero-title{position:absolute;top:208px;width:100%;text-align:center;color:var(--white);font-weight:700;font-size:24px;letter-spacing:-.3px}

  .services{position:absolute;top:433px;left:0;width:788px;height:248px;background:var(--section-light);box-shadow:0 -2px 4px rgba(0,0,0,.15)}
  .section-title{font-weight:400;font-size:12px;letter-spacing:1px;text-align:center}
  .services .section-title{margin-top:34px}
  .service{position:absolute;top:56px;width:130px;text-align:center}
  .service svg{display:block;margin:0 auto;height:48px}
  .service h3{font-weight:400;font-size:6.5px;letter-spacing:.5px;line-height:11px;margin-top:9px;text-transform:uppercase}
  .service p{font-size:6.5px;line-height:10.8px;color:var(--ink-soft);width:96px;margin:3px auto 0}
  .service .more{display:block;font-size:5.8px;letter-spacing:.5px;margin-top:12px;color:var(--ink);text-decoration:none}

  .about{position:absolute;top:681px;left:0;width:788px;height:172px;
    background:radial-gradient(ellipse at 20% 30%,#24325e 0,rgba(36,50,94,0) 40%),radial-gradient(ellipse at 85% 70%,#2a3868 0,rgba(42,56,104,0) 40%),var(--navy);color:var(--white)}
  .about .section-title{margin-top:26px;color:var(--white)}
  .about p{width:445px;margin:22px auto 0;text-align:center;font-size:8.6px;line-height:12px}

  .contact{position:absolute;top:853px;left:0;width:788px;height:313px;
    background:linear-gradient(110deg,#cfe7ec 0%,#f0f8fa 35%,#d4eaef 60%,#eef7f9 100%)}
  .contact .section-title{margin-top:24px}
  .field{position:absolute;border:1.6px solid var(--field-line);background:transparent;font-family:inherit;font-size:6px;color:#7a858c;padding:7px 8px;letter-spacing:.3px}
  .send{position:absolute;left:353px;top:213px;width:82px;height:23px;background:var(--navy-deep);color:var(--white);font-family:inherit;font-size:8px;font-weight:500;letter-spacing:.5px;border:none}
  .info{position:absolute;top:270px;display:flex;align-items:center;gap:10px;font-size:6px;color:var(--ink)}
  .info svg{width:13px;height:13px}

  .site-footer{position:absolute;top:1166px;left:0;width:788px;height:34px;background:var(--footer);color:var(--footer-text)}
  .site-footer small{position:absolute;left:158px;top:12px;font-size:6.5px}
  .social{position:absolute;top:11px;width:10px;height:10px;border-radius:50%;background:var(--footer-text)}
</style>
</head>
<body>
  <header class="hero">
    <div class="hero-art" role="img" aria-label="3D rendering of a protein molecule in blue, violet and red"></div>
    <div class="brand"><span>Velquor Labs</span><span class="brand-dot"></span></div>
    <nav class="main-nav">
      <a href="#">HOME</a><a href="#">ABOUT</a><a href="#">TECHNOLOGY</a><a href="#">PRODUCTS</a><a href="#">NEWS</a><a href="#">CONTACT</a>
    </nav>
    <h1 class="hero-title">SYNTHETIC BIOLOGY COMPANY</h1>
  </header>

  <section class="services">
    <h2 class="section-title">OUR SERVICES</h2>
    <div class="service" style="left:155px">
      <svg viewBox="0 0 60 48" fill="none" stroke="#111" stroke-width="2">
        <path d="M12 44 C20 30 38 20 48 4"/><path d="M20 46 C28 32 44 22 52 8"/>
        <path d="M18 36 l8 4 M24 28 l8 4 M32 20 l8 4 M40 12 l6 3"/>
      </svg>
      <h3>Better reproducibility from standard assays</h3>
      <p>Lorem ipsum dolor sit amet, consectetur adipiscing elit, sed do eiusmod tempor.</p>
      <a class="more" href="#">READ MORE</a>
    </div>
    <div class="service" style="left:332px">
      <svg viewBox="0 0 64 48" fill="none" stroke="#111" stroke-width="1.8">
        <circle cx="8" cy="24" r="4"/><circle cx="20" cy="20" r="5"/><circle cx="30" cy="30" r="4"/>
        <circle cx="38" cy="14" r="6"/><circle cx="42" cy="34" r="5"/><circle cx="54" cy="10" r="4"/><circle cx="54" cy="26" r="4"/>
        <path d="M12 23l3-1M24 24l3 3M33 26l3-7M34 31l3 2M43 11l7-1M44 16l7 7M50 28l-4 3"/>
      </svg>
      <h3>Eliminate bead<br>clumping</h3>
      <p>Lorem ipsum dolor sit amet, consectetur adipiscing elit, sed do eiusmod tempor.</p>
      <a class="more" href="#">READ MORE</a>
    </div>
    <div class="service" style="left:488px">
      <svg viewBox="0 0 64 48" fill="none" stroke="#111" stroke-width="1.8">
        <path d="M14 22l8-5 8 5v10l-8 5-8-5z"/><path d="M30 22l8-5 8 5v10l-8 5"/><path d="M38 17v-8l8-5 8 5v8l-8 5"/>
        <path d="M14 22l-6-3M14 32l-6 3M22 37v7M54 9l6-3"/>
      </svg>
      <h3>Minimal change to current workflow</h3>
      <p>Lorem ipsum dolor sit amet, consectetur adipiscing elit, sed do eiusmod tempor.</p>
      <a class="more" href="#">READ MORE</a>
    </div>
  </section>

  <section class="about" role="img" aria-label="Dark blue photo of molecular models behind the about text">
    <h2 class="section-title">ABOUT US</h2>
    <p>Velquor Labs is a Singapore-based synthetic biology company. We specialize in providing customized membrane protein products, services and expertise for drug discovery, diagnostics, and biomedical applications. Our company is backed by an international team of scientists, with diverse interdisciplinary backgrounds in synthetic chemistry, materials science, nanotechnology, cell signaling, and immunology. Our business team has extensive experience in biotechnology with a proven track record of working with small and big biotech and pharma companies all over the world.</p>
  </section>

  <section class="contact" role="img" aria-label="Pale blue photo of DNA strands behind the contact form">
    <h2 class="section-title">CONTACT US</h2>
    <div class="field" style="left:254px;top:56px;width:132px;height:23px">YOUR NAME</div>
    <div class="field" style="left:402px;top:56px;width:132px;height:23px">YOUR EMAIL</div>
    <div class="field" style="left:254px;top:92px;width:280px;height:108px">MESSAGE</div>
    <button class="send">SEND</button>
    <div class="info" style="left:158px">
      <svg viewBox="0 0 16 16"><path d="M3 1l3 0 1 4-2 1c1 2 3 4 5 5l1-2 4 1v3c0 1-1 2-2 2C7 15 1 9 1 3c0-1 1-2 2-2z" fill="#333"/></svg>
      <span>+ 3(071) 482 90 15</span>
    </div>
    <div class="info" style="left:318px">
      <svg viewBox="0 0 16 16"><path d="M8 1a5 5 0 0 1 5 5c0 4-5 9-5 9S3 10 3 6a5 5 0 0 1 5-5z" fill="#333"/><circle cx="8" cy="6" r="2" fill="#e1f0f3"/></svg>
      <span>SINGAPORE 618204</span>
    </div>
    <div class="info" style="left:498px">
      <svg viewBox="0 0 16 16" fill="none" stroke="#333" stroke-width="1.4"><rect x="1" y="3" width="14" height="10"/><path d="M1 3l7 6 7-6"/></svg>
      <span>hello@velquorlabs.com</span>
    </div>
  </section>

  <footer class="site-footer">
    <small>© 2015. Velquor Labs. All Rights Reserved.</small>
    <span class="social" style="left:597px"></span>
    <span class="social" style="left:621px"></span>
  </footer>
</body>
</html>
```